Tobias Grenfell Consulting

I've the wording, and the rough layout. See attached MicroSoft Word File. I need a professional to make my postcard "look pretty".

Consulting

```html
<!DOCTYPE html>
<html lang="en">
<head>
<meta charset="utf-8">
<title>Tobias Grenfell Consulting – Postcard</title>
<link rel="stylesheet" href="https://fonts.googleapis.com/css2?family=Roboto:wght@300;400;700&family=Arimo:wght@400;700&display=swap">
<style>
  :root {
    --blue: #2b8cb4;
    --blue-edge: #1f7599;
    --white: #ffffff;
    --yellow: #f6e71c;
    --ink: #333333;
    --rule: #555555;
    --frame-light: #4fb0d8;
    --frame-grey: #9a9a9a;
  }
  * { margin: 0; padding: 0; box-sizing: border-box; }
  html, body { width: 866px; height: 1200px; overflow: hidden; background: var(--white); }
  body { position: relative; font-family: "Arimo", Arial, sans-serif; color: var(--white); }

  /* Front side */
  .front { position: absolute; left: 0; top: 0; width: 866px; height: 577px; background: var(--blue); border-bottom: 1px solid var(--blue-edge); }
  .brand { position: absolute; left: 29px; top: 30px; width: 160px; height: 59px; border: 1px solid var(--white); display: flex; align-items: center; justify-content: center; text-align: center; font-family: "Roboto", Arial, sans-serif; font-weight: 300; font-size: 15px; line-height: 18px; color: var(--white); }
  .headline { position: absolute; left: 371px; top: 22px; font-family: "Roboto", Arial, sans-serif; font-weight: 300; font-size: 41px; line-height: 54px; color: var(--white); }
  .headline strong { font-weight: 700; }
  .headline .tail { display: block; padding-left: 140px; }
  .steps { position: absolute; left: 0; top: 0; }
  .step-label { position: absolute; font-weight: 700; font-size: 12.5px; line-height: 16px; color: var(--white); white-space: nowrap; }
  .intro-lead { position: absolute; right: 21px; top: 262px; text-align: center; font-weight: 700; font-size: 15.5px; line-height: 22px; color: var(--yellow); }
  .intro-body { position: absolute; left: 541px; top: 316px; width: 304px; font-size: 10.3px; line-height: 13.9px; text-align: justify; color: var(--white); }
  .intro-body p + p { margin-top: 14px; }

  /* Back side */
  .back-message { position: absolute; left: 0; top: 623px; width: 466px; height: 577px; background: var(--blue); border: 2px solid var(--frame-light); }
  .photo { position: absolute; left: 0; top: 0; width: 462px; height: 246px; background: linear-gradient(100deg, #2e2f33 0%, #6b6760 35%, #c9c2b6 65%, #e4ddd0 100%); }
  .photo-title { position: absolute; left: 270px; top: 160px; font-weight: 700; font-size: 30px; line-height: 34px; color: #3d3d3d; }
  .questions { position: absolute; left: 27px; top: 264px; width: 410px; font-size: 10.8px; line-height: 15.6px; list-style: none; }
  .closing { position: absolute; left: 27px; top: 420px; width: 395px; font-size: 10.8px; line-height: 15.6px; }
  .web { position: absolute; left: 27px; top: 544px; font-weight: 700; font-size: 14px; }
  .back-address { position: absolute; left: 466px; top: 623px; width: 400px; height: 577px; border: 1px solid var(--frame-grey); border-left: none; }
  .postage { position: absolute; left: 289px; top: 48px; font-weight: 700; font-size: 17px; line-height: 22px; color: var(--ink); }
  .address-line { position: absolute; left: 61px; width: 285px; height: 1px; background: var(--rule); }
</style>
</head>
<body>

<section class="front">
  <div class="brand">Tobias Grenfell<br>Consulting</div>

  <h1 class="headline">Learn Small Business<br>Success Secrets<br>only <strong>“insiders”</strong><span class="tail">know about:</span></h1>

  <svg class="steps" width="866" height="577" viewBox="0 0 800 533">
    <rect x="200" y="70" width="120" height="230" fill="#3597be" role="img" aria-label="Outline figure of a businessman with briefcase climbing the steps"/>
    <g fill="none" stroke="#ffffff" stroke-width="2.5" stroke-linejoin="round">
      <polyline points="20,460 44,460 108,353 143,375 175,319 215,255 262,255 276,318 296,262 320,262 339,298 377,213 465,162"/>
    </g>
    <polygon points="468,160 452,162 462,174" fill="#ffffff"/>
    <g fill="#ffffff">
      <circle cx="44" cy="460" r="7.5"/><circle cx="108" cy="353" r="7.5"/><circle cx="143" cy="375" r="7.5"/>
      <circle cx="175" cy="319" r="7.5"/><circle cx="276" cy="318" r="7.5"/><circle cx="339" cy="298" r="7.5"/>
      <circle cx="377" cy="213" r="7.5"/>
    </g>
    <g fill="#2b8cb4" font-family="Arimo, Arial, sans-serif" font-size="10" font-weight="700" text-anchor="middle">
      <text x="44" y="464">1</text><text x="108" y="357">2</text><text x="143" y="379">3</text>
      <text x="175" y="323">4</text><text x="276" y="322">5</text><text x="339" y="302">6</text><text x="377" y="217">7</text>
    </g>
  </svg>

  <span class="step-label" style="left:61px;top:494px">Key of scccess behind insiders point</span>
  <span class="step-label" style="left:36px;top:342px">Key of scccess<br>behind insiders point</span>
  <span class="step-label" style="left:166px;top:402px">Key of scccess behind insiders point</span>
  <span class="step-label" style="left:193px;top:358px">Key of scccess<br>behind insiders point</span>
  <span class="step-label" style="left:313px;top:343px">Key of scccess behind insiders point</span>
  <span class="step-label" style="left:383px;top:305px">Key of scccess behind<br>insiders point</span>
  <span class="step-label" style="left:407px;top:253px">Key of scccess behind<br>insiders point</span>

  <div class="intro-lead">Here just 6-7 line copy<br>(Always&nbsp; communication simple )</div>

  <div class="intro-body">
    <p>“Insiders” who know the answers to these tricky business problems, get ahead in business and life. And the deeper their understanding to these tricky business problems, the more successful they become. They have very little stress from their businesses; they work very few hours by building their businesses into "auto pilot". They have more free time to enjoy life.</p>
    <p>If you don't know how to solve these tricky business problems, you will find yourself struggling with your businesses. You will find yourself working very long hours, and you have a lot of stress from running your business. If you are not even aware of the existence of this aspect of running a business, your business will not survive. You will become part of the statistic: 80% of businesses fail.</p>
  </div>
</section>

<section class="back-message">
  <div class="photo" role="img" aria-label="Photo of a businessman's hand holding out an old key">
    <div class="photo-title">Key of<br>Success</div>
  </div>
  <ol class="questions">
    <li>1.How to make people want to have what you have for sale?</li>
    <li>2.How to turn new customers into repeat customers?</li>
    <li>3.How to make repeat customers comeback more often?</li>
    <li>4.How to spend less time with each customer, yet increase your profit on each business transaction?</li>
    <li>5.How to get more operating capital?</li>
    <li>6.How to buy low and sell high?</li>
    <li>7.How to manage employees and contractors?</li>
    <li>8.Which marketing methods are total waste of time and money?</li>
  </ol>
  <p class="closing">Why do 80% of all businesses fail??? Because their owners didn't know what “business insiders” know. They worked very long hours, they had a lot of stresses and headaches, and in the end, due to their lack of business know-how, their businesses failed and they were left with a bunch of debt, a broken heart and sometimes a broken family too. Don't become one of them! Become a real “insider”, run a successful business without stress and enjoy life! To find out more:</p>
  <div class="web">www.InsiderBusinessKeys.com</div>
</section>

<section class="back-address">
  <div class="postage">Postage<br>Paid</div>
  <div class="address-line" style="top:264px"></div>
  <div class="address-line" style="top:320px"></div>
  <div class="address-line" style="top:375px"></div>
  <div class="address-line" style="top:430px"></div>
</section>

</body>
</html>
```